Flyer for the Lumen 2025 Conference

I am looking to produce a flyer for our upcoming conference, Lumen 2025. This is an annual conference that we plan to publicize on social media. The ideal designer will create a flyer that is eye-catching and effectively communicates the key information. Please see attached our logo, speaker photo, and flyer content.

Target Market(s)

All demographics

Industry/Entity Type

Christian

Font styles to use
Sans Serif

Requirements
Should not have
• Cross, church

```html
<!DOCTYPE html>
<html lang="en">
<head>
<meta charset="UTF-8">
<title>Lumen 2025 Conference</title>
<link rel="stylesheet" href="https://fonts.googleapis.com/css2?family=Bebas+Neue&family=Montserrat:wght@500;600;700;800;900&display=swap">
<style>
  :root {
    --navy-top: #26268a;
    --navy-mid: #1a1a5e;
    --year-fill: #1c1c62;
    --ink: #050507;
    --gold: #eea52a;
    --gold-deep: #e4861f;
    --teal: #46c4d2;
    --white: #ffffff;
  }
  * { margin: 0; padding: 0; box-sizing: border-box; }
  html, body { width: 911px; height: 1200px; overflow: hidden; background: var(--ink); }
  .flyer {
    position: relative; width: 911px; height: 1200px; overflow: hidden;
    background: linear-gradient(180deg, var(--navy-top) 0%, var(--navy-mid) 45%, #0b0b24 72%, var(--ink) 88%);
    font-family: "Montserrat", sans-serif; color: var(--white);
  }
  .abs { position: absolute; }
  .photo-faint {
    left: 620px; top: 0; width: 291px; height: 380px;
    background: radial-gradient(ellipse at 60% 35%, rgba(70,70,170,.55), rgba(38,38,138,0) 70%);
  }
  .photo-speaker {
    left: 0; top: 230px; width: 390px; height: 820px;
    background: radial-gradient(ellipse at 45% 18%, #5a3d33 0%, #3a2a36 16%, rgba(31,80,160,.9) 34%, rgba(24,60,140,.75) 60%, rgba(10,10,30,0) 95%);
    -webkit-mask-image: linear-gradient(180deg, transparent 0, #000 10%, #000 70%, transparent 100%);
    mask-image: linear-gradient(180deg, transparent 0, #000 10%, #000 70%, transparent 100%);
  }
  .topic { left: 58px; top: 70px; }
  .label { color: var(--gold); font-weight: 800; font-size: 20px; letter-spacing: .5px; }
  .topic-title { font-weight: 900; font-size: 36px; line-height: 37px; letter-spacing: .3px; }
  .brand { left: 598px; top: 100px; display: flex; align-items: center; gap: 14px; }
  .brand-dot { width: 30px; height: 30px; border-radius: 50%; background: var(--gold-deep); }
  .brand-name { font-weight: 700; font-size: 58px; line-height: 1; letter-spacing: 2px; color: var(--white); }
  .title-main {
    left: 222px; top: 226px; font-weight: 900; font-size: 142px; line-height: 1; letter-spacing: 3px;
    background: linear-gradient(180deg, var(--gold-deep), var(--gold)); -webkit-background-clip: text; background-clip: text; color: transparent;
  }
  .title-year {
    left: 236px; top: 343px; font-weight: 700; font-size: 236px; line-height: 1; letter-spacing: -6px;
    color: var(--year-fill);
    text-shadow:
      3px 0 0 var(--white), -3px 0 0 var(--white), 0 3px 0 var(--white), 0 -3px 0 var(--white),
      2px 2px 0 var(--white), -2px 2px 0 var(--white), 2px -2px 0 var(--white), -2px -2px 0 var(--white),
      3px 1px 0 var(--white), -3px 1px 0 var(--white), 3px -1px 0 var(--white), -3px -1px 0 var(--white),
      1px 3px 0 var(--white), -1px 3px 0 var(--white), 1px -3px 0 var(--white), -1px -3px 0 var(--white);
  }
  .prophetic { right: 58px; top: 584px; font-family: "Bebas Neue", sans-serif; font-size: 100px; line-height: 1; color: var(--gold); }
  .conference { right: 58px; top: 682px; font-weight: 800; font-size: 52px; line-height: 1; letter-spacing: 1px; }
  .dates { left: 383px; top: 783px; display: flex; gap: 22px; }
  .date-card {
    width: 146px; height: 183px; border: 2px solid var(--gold); text-align: center; padding-top: 12px;
  }
  .date-month { font-family: "Bebas Neue", sans-serif; font-size: 30px; line-height: 28px; color: var(--teal); }
  .date-day { font-family: "Bebas Neue", sans-serif; font-size: 62px; line-height: 50px; color: var(--white); }
  .date-weekday { font-weight: 800; font-size: 19px; line-height: 24px; color: var(--gold); }
  .time { width: 102px; margin: 0 auto; font-weight: 700; font-size: 16px; line-height: 19px; color: var(--white); }
  .time-start { background: var(--gold); margin-top: 3px; }
  .time-end { background: var(--teal); margin-top: 7px; }
  .speaker { left: 56px; top: 886px; width: 250px; text-align: center; }
  .speaker .label { font-size: 17px; }
  .speaker-name { font-weight: 800; font-size: 24px; line-height: 26px; }
  .app { left: 74px; top: 1012px; }
  .app-line { font-weight: 500; font-size: 15px; line-height: 19px; }
  .app-name { font-weight: 800; font-size: 21px; line-height: 24px; color: var(--gold); }
  .store-badge { left: 72px; width: 106px; height: 31px; border-radius: 6px; background: var(--white); }
  .contacts { left: 188px; top: 1090px; }
  .contact { display: flex; align-items: center; gap: 8px; font-weight: 500; font-size: 16px; line-height: 23px; }
  .contact svg { width: 17px; height: 17px; }
  .location { right: 71px; top: 1032px; text-align: right; }
  .location-script { display: inline-block; width: 96px; height: 24px; background: rgba(238,165,42,.3); border-radius: 3px; margin-bottom: 6px; }
  .venue { font-weight: 800; font-size: 14px; line-height: 18px; }
  .address { font-weight: 500; font-size: 14px; line-height: 18px; }
  .location-frame { left: 600px; top: 1028px; width: 254px; height: 132px; }
</style>
</head>
<body>
<main class="flyer">
  <div class="abs photo-faint" role="img" aria-label="Faint close-up portrait of the speaker"></div>
  <div class="abs photo-speaker" role="img" aria-label="Portrait of the speaker in a blue suit and grey turtleneck"></div>

  <section class="abs topic">
    <div class="label">TOPIC:</div>
    <div class="topic-title">THE VOICE<br>OF THE LORD</div>
  </section>

  <div class="abs brand">
    <span class="brand-dot"></span>
    <span class="brand-name">VESSA</span>
  </div>

  <h1 class="abs title-main">LUMEN</h1>
  <div class="abs title-year">2025</div>
  <div class="abs prophetic">A PROPHETIC</div>
  <div class="abs conference">CONFERENCE</div>

  <section class="abs dates">
    <div class="date-card">
      <div class="date-month">DECEMBER</div>
      <div class="date-day">26TH</div>
      <div class="date-weekday">FRIDAY</div>
      <div class="time time-start">6:30 PM</div>
      <div class="time time-end">9:00 PM</div>
    </div>
    <div class="date-card">
      <div class="date-month">DECEMBER</div>
      <div class="date-day">27TH</div>
      <div class="date-weekday">SATURDAY</div>
      <div class="time time-start">5:30 PM</div>
      <div class="time time-end">8:00 PM</div>
    </div>
    <div class="date-card">
      <div class="date-month">DECEMBER</div>
      <div class="date-day">29TH</div>
      <div class="date-weekday">SUNDAY</div>
      <div class="time time-start">4:30 PM</div>
      <div class="time time-end">7:00 PM</div>
    </div>
  </section>

  <section class="abs speaker">
    <div class="label">SPEAKER:</div>
    <div class="speaker-name">PROPHET<br>ELIAS MBEKI</div>
  </section>

  <section class="abs app">
    <div class="app-line">Download the</div>
    <div class="app-name">VESSA APP</div>
    <div class="app-line">to stay updated on the event</div>
  </section>
  <div class="abs store-badge" style="top:1090px"></div>
  <div class="abs store-badge" style="top:1126px"></div>

  <section class="abs contacts">
    <div class="contact">
      <svg viewBox="0 0 20 20"><circle cx="10" cy="10" r="10" fill="#eea52a"/><rect x="7" y="4.5" width="6" height="11" rx="1.2" fill="none" stroke="#050507" stroke-width="1.4"/></svg>
      555 013 4270
    </div>
    <div class="contact">
      <svg viewBox="0 0 20 20"><circle cx="10" cy="10" r="10" fill="#eea52a"/><rect x="5" y="6.5" width="10" height="7" rx="1" fill="none" stroke="#050507" stroke-width="1.4"/><path d="M5 7l5 4 5-4" fill="none" stroke="#050507" stroke-width="1.4"/></svg>
      contact@vessa.org
    </div>
    <div class="contact">
      <svg viewBox="0 0 20 20"><circle cx="10" cy="10" r="10" fill="#eea52a"/><circle cx="10" cy="10" r="5" fill="none" stroke="#050507" stroke-width="1.3"/><path d="M5 10h10M10 5c-2.5 3-2.5 7 0 10M10 5c2.5 3 2.5 7 0 10" fill="none" stroke="#050507" stroke-width="1.1"/></svg>
      www.vessa.org
    </div>
  </section>

  <svg class="abs location-frame" viewBox="0 0 254 132" fill="none">
    <path d="M253 2V122a8 8 0 0 1-8 8H0" stroke="#eea52a" stroke-width="1.5"/>
  </svg>
  <section class="abs location">
    <span class="location-script" role="img" aria-label="Handwritten word Location"></span>
    <div class="venue">The Harborview<br>Performing Arts Center</div>
    <div class="address">218 Linden Street<br>Fairhaven, Maine 04099</div>
  </section>
</main>
</body>
</html>
```